Law Offices business card

Hi there, I'll need business card for the Law Offices of Tobin Haskell. The information must convey his strategic approach and quick resolution to complex business litigation needs. Please emphasize Civil Litigation, Corporate Law, Business Governance and Real Estate Law. Tobin has over 25 years of experience in these fields.The card should be modern and edgy and the message should be clear. Please consult his current website for ideas.

Business

```html
<!DOCTYPE html>
<html lang="en">
<head>
<meta charset="utf-8">
<title>Law Offices of Tobin Haskell – Business Card</title>
<link rel="stylesheet" href="https://fonts.googleapis.com/css2?family=Arimo:wght@400;700&display=swap">
<style>
  :root {
    --page-bg: #3a3a3c;
    --card-black: #0b0b0c;
    --card-black-soft: #1c1c1e;
    --brand-red: #c44f4d;
    --accent-red: #b3332f;
    --ink-light: #ffffff;
    --ink-muted: #bdbdbd;
  }
  * { box-sizing: border-box; margin: 0; padding: 0; }
  html, body {
    width: 1200px; height: 950px; overflow: hidden;
    background: var(--page-bg);
    font-family: "Arimo", Arial, sans-serif;
  }
  .canvas { position: relative; width: 1200px; height: 950px; }
  .card {
    position: absolute; left: 250px; width: 700px; height: 400px;
    overflow: hidden;
    box-shadow: 0 10px 30px rgba(0,0,0,.45);
  }

  /* Back side */
  .card-back {
    top: 50px;
    background: linear-gradient(160deg, var(--card-black-soft) 0%, var(--card-black) 60%);
  }
  .card-back .brand {
    position: absolute; top: 120px; left: 0; right: 0;
    display: flex; align-items: center; justify-content: center; gap: 14px;
  }
  .brand-square { width: 22px; height: 22px; background: var(--accent-red); flex: none; }
  .brand-name {
    color: var(--ink-light); font-weight: 400; font-size: 30px; letter-spacing: 1px;
  }
  .practice {
    position: absolute; top: 190px; left: 40px; right: 40px;
    text-align: center; color: var(--ink-muted);
  }
  .practice-areas { font-size: 13px; letter-spacing: 1.5px; text-transform: uppercase; }
  .practice-areas .sep { color: var(--accent-red); margin: 0 6px; }
  .experience { margin-top: 10px; font-size: 13px; letter-spacing: 1px; }
  .card-back .web-line {
    position: absolute; top: 300px; left: 0; right: 0;
    display: flex; align-items: center; justify-content: center; gap: 16px;
  }
  .rule { width: 90px; height: 2px; background: var(--accent-red); }
  .web-address { color: var(--ink-muted); font-size: 17px; letter-spacing: 5px; }

  /* Front side */
  .card-front { top: 500px; display: flex; background: var(--card-black); }
  .contact-panel {
    width: 285px; height: 100%; flex: none;
    background: var(--brand-red); color: var(--ink-light);
    padding: 78px 0 0 40px;
  }
  .person-name { font-size: 25px; font-weight: 700; line-height: 1.1; }
  .person-role { font-size: 17px; margin-bottom: 14px; }
  .address { font-size: 16px; line-height: 1.35; margin-bottom: 6px; }
  .contact-list { list-style: none; font-size: 15px; }
  .contact-list li { display: flex; align-items: center; gap: 10px; height: 24px; white-space: nowrap; }
  .contact-list svg { width: 16px; height: 16px; fill: var(--ink-light); flex: none; }
  .divider { width: 4px; height: 100%; background: var(--ink-light); flex: none; }
  .logo-panel {
    flex: 1; height: 100%;
    background: linear-gradient(150deg, var(--card-black-soft) 0%, var(--card-black) 55%);
    display: flex; align-items: center; justify-content: center;
  }
  .firm-logo { display: flex; align-items: center; gap: 14px; }
  .firm-name {
    color: var(--ink-light); font-weight: 400; font-size: 22px; line-height: 1.25; letter-spacing: .5px;
  }
</style>
</head>
<body>
<main class="canvas">

  <section class="card card-back" aria-label="Card back">
    <div class="brand">
      <span class="brand-square"></span>
      <span class="brand-name">Tobin Haskell</span>
    </div>
    <div class="practice">
      <p class="practice-areas">Civil Litigation<span class="sep">|</span>Corporate Law<span class="sep">|</span>Business Governance<span class="sep">|</span>Real Estate Law</p>
      <p class="experience">Over 25 years of strategic, efficient resolution</p>
    </div>
    <div class="web-line">
      <span class="rule"></span>
      <span class="web-address">www.haskell-law.example</span>
      <span class="rule"></span>
    </div>
  </section>

  <section class="card card-front" aria-label="Card front">
    <div class="contact-panel">
      <p class="person-name">Marcus Hale</p>
      <p class="person-role">President</p>
      <p class="address">2710 Alder Crest Lane<br>Linden Hollow, NY 11290</p>
      <ul class="contact-list">
        <li><svg viewBox="0 0 16 16"><path d="M3 1h3l1.5 4-2 1.2a9 9 0 0 0 4.3 4.3L11 8.5l4 1.5v3a2 2 0 0 1-2 2A12 12 0 0 1 1 3a2 2 0 0 1 2-2z"/></svg>555 0142 2253</li>
        <li><svg viewBox="0 0 16 16"><path d="M4 0h8a1 1 0 0 1 1 1v14a1 1 0 0 1-1 1H4a1 1 0 0 1-1-1V1a1 1 0 0 1 1-1zm1 2v10h6V2zm3 11a1 1 0 1 0 0 2 1 1 0 0 0 0-2z"/></svg>555 0187 5335</li>
        <li><svg viewBox="0 0 16 16"><path d="M4 1h8v4H4zM2 6h12a1 1 0 0 1 1 1v6h-3v2H4v-2H1V7a1 1 0 0 1 1-1zm3 5v3h6v-3z"/></svg>555 0163 3856</li>
        <li><svg viewBox="0 0 16 16"><path d="M1 3h14v10H1zm1.5 1.3V12h11V4.3L8 8.8z M2.8 4 8 7.8 13.2 4z"/></svg>marcus@haskell-law.example</li>
        <li><svg viewBox="0 0 16 16"><path d="M8 1a7 7 0 1 0 0 14A7 7 0 0 0 8 1zm-1 3h2v4.5l3 1.8-1 1.6L7 9.5z"/></svg>www.haskell-law.example</li>
      </ul>
    </div>
    <div class="divider"></div>
    <div class="logo-panel">
      <div class="firm-logo">
        <span class="brand-square"></span>
        <p class="firm-name">Law Offices of<br>Tobin Haskell, PA</p>
      </div>
    </div>
  </section>

</main>
</body>
</html>
```